Norwegian Mobile Home/Cabin Producer Needs Brochure Design

We make and deliver our own brand of mobile homes especially made for Norway and it's weather conditions. We differ from other brands in building quality in regards to a much more solid construction, insulation and choices. We work with our customer from the beginning and build them after their demands and wishes.
We need a brochure that holds us out as top of the line. We deliver mobile homes of all kinds and sizes. Both to the private and professional sector.
For the professional sector, mainly camping sites we want to show, lodges-, sanitary- and kitchen wagoons etc.
So we need a brochure of 14-20 pages in A4 where the double pages can be printed in A3 format.
We have logo (provided). But we need cover as well as back suggestions.
It should start with pages where we can teel who we are and stand for.Piicture(s) and space for some editable text (which we can write in norwegian). The text part can have a transparent background......or not. Give us your best shot. Also a smaller part in the private sector that shows winter time.
We want other pages for the private sector that shows what we deliver and the possibilities of choices.
Pages for the the professional sector.
Pages that show our production. How we transport. And the split construction. Only pictures from this portfolio here. (see fotoskap portfolios)
Take a look at provided pictures and our website www.solvikhytta.no for inspiration.
Here's a FotoSkap link to Pictures to choose from. http://bildelagr.example/K4TQ9P
(Hope it Works, let me know if not)
Our company name in small letters "fjordgrønn hyttebygg" means directly translated "fjordgreen cabin builds".
Looking forward to your suggestions.
Target Market(s)
Private market for vacation mobile homes. Camping sites and similar
Industry/Entity Type
Insulation
Requirements
Must have
- Our logo on the front page. Simple but inviting and professional
Logo and address on the back.

```html
<!DOCTYPE html>
<html lang="en">
<head>
<meta charset="utf-8">
<title>Our goal – fjordgrønn hyttebygg as</title>
<link rel="stylesheet" href="https://fonts.googleapis.com/css2?family=Open+Sans:wght@400;600&family=Nunito:wght@700&display=swap">
<style>
  :root {
    --brand-blue: #2d5282;
    --ink-black: #0b0b0b;
    --paper: #ffffff;
    --text-light: #ffffff;
    --rule-grey: #c4c4c4;
    --rule-warm: #c98a4a;
    --name-grey: #6e6e6e;
    --edge-line: #f3d9c8;
  }
  html, body {
    margin: 0;
    padding: 0;
    overflow: hidden;
    background: var(--paper);
  }
  .page {
    position: relative;
    width: 851px;
    height: 1200px;
    overflow: hidden;
    background: var(--paper);
    font-family: "Open Sans", sans-serif;
    border-left: 1px solid var(--edge-line);
    box-sizing: border-box;
  }
  .page::after {
    content: "";
    position: absolute;
    top: 0;
    bottom: 0;
    left: 831px;
    width: 1px;
    background: var(--edge-line);
  }
  .title-block {
    position: absolute;
    left: 21px;
    top: 3px;
    width: 232px;
    height: 396px;
    margin: 0;
    background: var(--brand-blue);
    color: var(--text-light);
    font-weight: 400;
  }
  .title-block .word {
    position: absolute;
    line-height: 1;
    letter-spacing: -5px;
    text-shadow: 0 16px 7px rgba(0, 0, 0, 0.42);
  }
  .title-block .word-our {
    top: 118px;
    left: 6px;
    font-size: 128px;
  }
  .title-block .word-goal {
    top: 243px;
    right: 10px;
    font-size: 88px;
    letter-spacing: -4px;
  }
  .photo {
    position: absolute;
    left: 270px;
    width: 531px;
  }
  .photo-reception {
    top: 0;
    height: 513px;
    background:
      radial-gradient(ellipse 60% 30% at 45% 32%, rgba(255, 255, 255, 0.18), transparent 70%),
      linear-gradient(180deg, #5e6a3e 0%, #9d8a62 12%, #4a4e48 28%, #3a3f3c 42%, #8c7e6c 58%, #b4a898 78%, #c9bfb1 100%);
  }
  .photo-cabin {
    top: 563px;
    height: 515px;
    background:
      radial-gradient(ellipse 55% 18% at 55% 26%, rgba(240, 238, 232, 0.55), transparent 75%),
      linear-gradient(180deg, #3c5b31 0%, #4f6848 18%, #5a6b80 30%, #8a9a6a 46%, #7b9447 58%, #6b8342 72%, #55654a 86%, #7f8466 100%);
  }
  .band {
    position: absolute;
    left: 270px;
    width: 531px;
    background: var(--ink-black);
  }
  .band-middle {
    top: 513px;
    height: 50px;
  }
  .band-bottom {
    top: 1078px;
    height: 122px;
  }
  .rule {
    position: absolute;
    z-index: 2;
  }
  .rule-middle {
    left: 191px;
    top: 536px;
    width: 564px;
    height: 1px;
    background: var(--rule-grey);
  }
  .rule-warm {
    left: 345px;
    top: 563px;
    width: 456px;
    height: 1px;
    background: var(--rule-warm);
  }
  .rule-lower {
    left: 271px;
    top: 1034px;
    width: 504px;
    height: 2px;
    background: var(--text-light);
  }
  .intro-panel {
    position: absolute;
    z-index: 1;
    left: 84px;
    top: 428px;
    width: 261px;
    height: 578px;
    background: var(--brand-blue);
    color: var(--text-light);
    box-sizing: border-box;
    padding: 118px 15px 0 14px;
    font-size: 19px;
    line-height: 36.6px;
  }
  .intro-panel p {
    margin: 0 0 36.6px;
  }
  .intro-panel .line {
    display: block;
    text-align: justify;
    text-align-last: justify;
    white-space: nowrap;
  }
  .intro-panel .line-spaced {
    letter-spacing: 7px;
  }
  .company-name {
    position: absolute;
    left: 23px;
    top: 1120px;
    margin: 0;
    font-family: "Nunito", sans-serif;
    font-weight: 700;
    font-size: 20px;
    color: var(--name-grey);
    white-space: nowrap;
  }
  .tagline {
    position: absolute;
    left: 282px;
    top: 1148px;
    margin: 0;
    font-size: 28px;
    letter-spacing: 10px;
    color: var(--text-light);
    white-space: nowrap;
  }
</style>
</head>
<body>
<main class="page">
  <div class="photo photo-reception" role="img" aria-label="Photo of a thatched-roof reception cabin with a red and white barrier arm in front, under tall trees"></div>
  <div class="band band-middle"></div>
  <div class="photo photo-cabin" role="img" aria-label="Photo of a white holiday cabin with red shutters beside a pond with reeds and water lilies"></div>
  <div class="band band-bottom"></div>
  <div class="rule rule-middle"></div>
  <div class="rule rule-warm"></div>
  <div class="rule rule-lower"></div>

  <h1 class="title-block">
    <span class="word word-our">Our</span>
    <span class="word word-goal">goal</span>
  </h1>

  <section class="intro-panel">
    <p>
      <span class="line">Who we are who we</span>
      <span class="line">are who we are &nbsp; Who</span>
      <span class="line">we are who we are</span>
      <span class="line line-spaced">who we are .</span>
    </p>
    <p>
      <span class="line">Who we are who we</span>
      <span class="line">are who we are &nbsp; Who</span>
      <span class="line">we are who we are</span>
      <span class="line">who we are . Who we</span>
      <span class="line">are who we are who we</span>
      <span class="line">are &nbsp; Who we are who</span>
      <span class="line">we are who we are .</span>
    </p>
  </section>

  <p class="company-name">fjordgrønn hyttebygg as</p>
  <p class="tagline">to give you the best...</p>
</main>
</body>
</html>
```